International Flower distributer needs a landing page

We are looking to have a landing page made that will be easy to maintain and upload more content as our business grows.

We like the template designs and ease of use of Pagewright. We'd explore other host sites.

Hello,

To start we would like something that can be managed and updated on a platform like pagewright. We like page wright because of the premade designs and flexibility.

Website requirements:

- About us:

- Marlowe Vantage Corp - Established 1999

- Verna Holt - Founder

- Danielle Holt - Account Executive

- Gregory Holt - Director of Operations

- Pilar Wendham - (Jo's Job Description?)

- Renata Valcourt (Make us look like a bigger company with more staff)

What we do:

- Personalized Customer service

- Exclusively Mass market experience to meet high demands

- Dedicated team assigned to your account

How we do it:

- Partnerships with farms in COlombia, ecuador and costa rica

- Farm fresh delivered directly from cargo planes to state of the art cooler facility at Delmont Airport

- Verity Trust?

Products we Sell:

- Farm made bouquets

- Consumer Bunches

- Programs Tailored to fit customer's retail program

For more Information:

- Gregory and Danielle phone and email

- Submit email inquiry

Gathering more feedback

Corporate buyers that want to verify who we are and get our contact information

Floral, but not a flower shop. We import farm fresh cut flowers from south america and send them directly to supermarkets around the country.

• We are not selling anything on the website. We sell business to business.

```html
<!DOCTYPE html>
<html lang="en">
<head>
<meta charset="utf-8">
<title>Marlowe Vantage — International Flower Distributor</title>
<link rel="stylesheet" href="https://fonts.googleapis.com/css2?family=Arimo:wght@400;700&display=swap">
<style>
:root{
  --green:#79b530;
  --green-dark:#5f9a1f;
  --ink:#1c1c1c;
  --text:#4a4a4a;
  --navy:#2f3f9c;
  --ring:#2e3d8f;
  --night:#24161b;
  --white:#ffffff;
}
*{margin:0;padding:0;box-sizing:border-box}
html,body{width:1200px;height:4882px;overflow:hidden}
body{position:relative;font-family:"Arimo",Arial,sans-serif;color:var(--text);background:var(--white)}
.abs{position:absolute}
.center{text-align:center}
h1,h2,h3,h4{font-weight:400}
.title{font-size:40px;color:var(--ink);letter-spacing:.5px;text-align:center;font-weight:400}
.title b{font-weight:700}
.title-rule{width:52px;height:3px;background:var(--green);margin:10px auto 0}
.intro{font-size:15px;line-height:29px;text-align:center;color:#555;width:800px;left:200px}
.btn{display:flex;align-items:center;justify-content:center;background:var(--green);color:#fff;font-weight:700;font-size:14px;border-radius:24px;letter-spacing:.5px}

/* hero */
.hero{left:0;top:0;width:1200px;height:640px;background:linear-gradient(160deg,#2f4a1c 0%,#5b7a2a 30%,#d9a3d6 55%,#e9c84a 80%,#6a8a2a 100%)}
.hero-rule{left:0;top:640px;width:1200px;height:3px;background:var(--green)}
.topbar{top:22px;left:600px;width:500px;display:flex;gap:22px;justify-content:flex-end;font-size:14px;color:#fff;align-items:center}
.topbar .ico{display:inline-flex;gap:10px}
.topbar .dot{width:10px;height:10px;border-radius:50%;background:#fff;display:inline-block}
.nav{top:62px;left:482px;display:flex;gap:25px;font-size:15px;font-weight:700;color:#fff;letter-spacing:.3px}
.brand{display:flex;align-items:center;gap:12px;color:#fff;font-weight:700;font-size:24px;line-height:26px;letter-spacing:1px}
.brand .mark{width:64px;height:64px;border-radius:50%;border:3px solid #fff}
.hero-title{top:232px;left:99px;color:#fff;font-size:42px;line-height:48px;letter-spacing:.5px;font-weight:400}
.hero-title b{font-weight:700}
.hero-sub{top:336px;left:99px;width:480px;color:#fff;font-size:15px;line-height:25px}

/* what we do */
.wwd{left:0;top:643px;width:1200px;height:872px;background:linear-gradient(180deg,#fbf6f8 0%,#f4e6ee 45%,#e9d3e0 100%)}
.service{width:320px;text-align:center}
.service .pic{width:250px;height:250px;border-radius:50%;margin:0 auto}
.service h3{margin-top:24px;font-size:17px;line-height:26px;color:var(--ink);font-weight:700}
.service p{margin-top:14px;font-size:12px;line-height:22px;color:#555}

/* about */
.about-bg{left:0;top:1515px;width:1200px;height:531px;background:linear-gradient(100deg,#f0e4ea 0%,#f2b7d4 40%,#e65a9e 65%,#c2387e 85%,#6a8a3a 100%)}
.about-card{left:112px;top:1464px;width:425px;height:472px;background:#fff;box-shadow:0 4px 20px rgba(0,0,0,.12);text-align:center}
.about-card .seal{width:95px;height:95px;border-radius:50%;border:4px solid var(--ring);margin:24px auto 0}
.about-card h2{margin-top:18px;font-size:40px;color:var(--ink);font-weight:400}
.about-card h2 b{font-weight:700}
.about-card p{margin:14px 24px 0;font-size:14px;line-height:27px;color:#555}

/* products */
.product .pic{width:313px;height:368px}
.product h3{margin-top:20px;font-size:21px;line-height:28px;color:var(--ink);text-align:center;font-weight:700}

/* reviews */
.reviews{left:0;top:2835px;width:1200px;height:593px;background:linear-gradient(180deg,#34419f 0%,#3d55a0 45%,#5f8f58 80%,#79b530 100%)}
.review{width:315px;height:246px;background:#fff;padding:16px 13px}
.review .quote{font-size:40px;line-height:30px;color:var(--green);font-weight:700;font-family:Georgia,serif}
.review p{margin-top:4px;font-size:12.5px;line-height:24px;color:#666}
.review .who{position:absolute;left:13px;bottom:14px;font-size:13px;font-weight:700;color:var(--ink);line-height:14px}
.review .who span{display:block;font-weight:400;font-size:10px;color:#888}
.review .badge{position:absolute;right:14px;bottom:14px;width:80px;height:28px;border-radius:4px;background:#e6ebf5}
.pager{top:3348px;left:556px;display:flex;gap:12px}
.pager i{width:11px;height:11px;border-radius:50%;border:2px solid #fff;display:block}
.pager i.on{background:#fff}

/* how we do it */
.how{width:318px;height:376px;background:#f6f6f4}
.how .pic{width:318px;height:230px}
.how .cap{height:146px;display:flex;align-items:center;justify-content:center;text-align:center;font-size:16px;line-height:27px;font-weight:700;color:var(--ink)}

/* contact + footer */
.night{left:0;top:4169px;width:1200px;height:713px;background:linear-gradient(180deg,#2a1a1f 0%,#231418 60%,#2a161c 100%)}
.field{background:#fff;height:42px;font-size:13px;color:#777;padding:14px 20px}
.footer-col h4{font-size:14px;font-weight:700;color:#fff;letter-spacing:.3px}
.footer-col ul{list-style:none;margin-top:10px}
.footer-col li{font-size:13px;line-height:24.5px;color:#fff}
.footer-col li::before{content:"» ";color:#fff}
.contact li::before{content:none}
.contact li{display:flex;gap:8px;align-items:flex-start;line-height:22px}
.contact .name{font-weight:700;padding-left:18px}
.contact svg{flex:none;margin-top:5px}
.social{width:44px;height:44px;border-radius:50%;background:#fff}
</style>
</head>
<body>

<!-- HERO -->
<div class="abs hero" role="img" aria-label="Photograph of pink daisies among yellow flowers in a field"></div>
<div class="abs hero-rule"></div>
<div class="abs brand" style="left:99px;top:14px">
  <span class="mark"></span>
  <span>MARLOWE<br>VANTAGE</span>
</div>
<div class="abs topbar">
  <span>
    <svg width="12" height="12" viewBox="0 0 24 24" fill="#fff"><path d="M6.6 10.8a15 15 0 0 0 6.6 6.6l2.2-2.2a1 1 0 0 1 1-.25 11 11 0 0 0 3.6.6 1 1 0 0 1 1 1V20a1 1 0 0 1-1 1A17 17 0 0 1 3 4a1 1 0 0 1 1-1h3.5a1 1 0 0 1 1 1 11 11 0 0 0 .6 3.6 1 1 0 0 1-.25 1z"/></svg>
    410-555-0182</span>
  <span>
    <svg width="14" height="10" viewBox="0 0 14 10"><rect width="14" height="10" fill="#fff"/><path d="M0 0l7 6 7-6" stroke="#555" fill="none"/></svg>
    Danielle@marlowevantage.com</span>
  <span class="ico"><i class="dot"></i><i class="dot"></i><i class="dot"></i><i class="dot"></i></span>
</div>
<nav class="abs nav">
  <span>ABOUT US</span><span>WHAT WE DO</span><span>HOW WE DO IT</span><span>OUR PRODUCTS</span><span>CONTACT US</span>
</nav>
<h1 class="abs hero-title"><b>INTERNATIONAL</b><br>FLOWER <b>DISTRIBUTER</b></h1>
<p class="abs hero-sub">We import farm fresh cut flowers from south america &amp; send them directly to supermarkets around the country.</p>
<div class="abs btn" style="left:99px;top:406px;width:185px;height:46px">OUR PRODUCTS</div>

<!-- WHAT WE DO -->
<section class="abs wwd" role="img" aria-label="Faded photograph of a flower farm greenhouse"></section>

<div class="abs" style="left:0;top:795px;width:1200px">
  <h2 class="title"><b>WHAT</b> WE DO</h2><div class="title-rule"></div>
</div>
<p class="abs intro" style="top:877px">Lorem ipsum dolor sit amet, consectetur adipiscing elit, sed do eiusmod tempor incididunt ut labore et dolore magna aliqua. Quis ipsum suspendisse ultrices gravida. Risus commodo viverra maecenas</p>

<div class="abs service" style="left:90px;top:982px">
  <div class="pic" role="img" aria-label="Photo of a florist handing a bouquet to a customer" style="background:linear-gradient(135deg,#3b3a3a,#8d6b56,#2f3d52)"></div>
  <h3>Personalized Customer<br>service</h3>
  <p>Lorem ipsum dolor sit amet, consectetur adipiscing elit, sed do eiusmod tempor incididunt ut labore et dolore magna aliqua.</p>
</div>
<div class="abs service" style="left:441px;top:982px">
  <div class="pic" role="img" aria-label="Photo of a market stall full of mixed flower bunches" style="background:linear-gradient(135deg,#6b8a3a,#d9446a,#e7c04a,#7a3a6a)"></div>
  <h3>Exclusively Mass market<br>experience to meet high demands</h3>
  <p>Lorem ipsum dolor sit amet, consectetur adipiscing elit, sed do eiusmod tempor incididunt ut labore et dolore magna aliqua.</p>
</div>
<div class="abs service" style="left:790px;top:982px">
  <div class="pic" role="img" aria-label="Photo of three staff members in aprons" style="background:linear-gradient(135deg,#2f4a6a,#c9a48a,#2a3a5a)"></div>
  <h3>Dedicated team assigned to<br>your account</h3>
  <p>Lorem ipsum dolor sit amet, consectetur adipiscing elit, sed do eiusmod tempor incididunt ut labore et dolore magna aliqua.</p>
</div>

<!-- ABOUT -->
<section class="abs about-bg" role="img" aria-label="Photograph of pink chrysanthemums with white flowers"></section>
<div class="abs about-card">
  <div class="seal"></div>
  <h2><b>ABOUT</b> US</h2>
  <p>Lorem ipsum dolor sit amet, kidunt ut labore et dolore magna aliqua. Quis ipsumuspendisse ultrices gravida. Risus commodo vivea maecenas accumsan lacus vel facilisis. Lorum dolor sit amet, consectetur adipiscing elit, sed do eiusmod tempor idunt ut labore et dolore magna aliqua. Quis ipsususpendisse ultrices gravida. Risus commodo viverra maecenas</p>
  <div class="btn" style="width:186px;height:47px;margin:20px auto 0">LEARN MORE</div>
</div>

<!-- PRODUCTS -->
<div class="abs" style="left:0;top:2130px;width:1200px">
  <h2 class="title"><b>OUR</b> PRODUCTS</h2><div class="title-rule"></div>
</div>
<p class="abs intro" style="top:2212px">Lorem ipsum dolor sit amet, consectetur adipiscing elit, sed do eiusmod tempor incididunt ut labore et dolore magna aliqua. Quis ipsum suspendisse ultrices gravida. Risus commodo viverra maecenas</p>
<div class="abs product" style="left:100px;top:2309px">
  <div class="pic" role="img" aria-label="Photo of a woman smelling sunflowers in a field" style="background:linear-gradient(150deg,#e9852a,#3f6b2a,#d9a23a)"></div>
  <h3>Farm made<br>bouquets</h3>
</div>
<div class="abs product" style="left:442px;top:2309px">
  <div class="pic" role="img" aria-label="Photo of a hand holding a mixed consumer bunch" style="background:linear-gradient(150deg,#f2eee6,#e78aa0,#8cb85a,#f3f0ea)"></div>
  <h3>Consumer<br>Bunches</h3>
</div>
<div class="abs product" style="left:785px;top:2309px">
  <div class="pic" role="img" aria-label="Photo of two growers with a potted plant in a greenhouse" style="background:linear-gradient(150deg,#c9d3cf,#d8456a,#f0f0ea,#e0406a)"></div>
  <h3>Programs Tailored to fit<br>customer's retail program</h3>
</div>

<!-- REVIEWS -->
<section class="abs reviews"></section>
<div class="abs" style="left:0;top:2894px;width:1200px">
  <h2 class="title" style="color:#fff"><b>CUSTOMERS</b> REVIEWS</h2><div class="title-rule"></div>
</div>
<p class="abs intro" style="top:2976px;color:#fff">Lorem ipsum dolor sit amet, consectetur adipiscing elit, sed do eiusmod tempor incididunt ut labore et dolore magna aliqua. Quis ipsum suspendisse ultrices gravida. Risus commodo viverra maecenas</p>
<div class="abs review" style="left:100px;top:3070px">
  <div class="quote">&ldquo;&ldquo;</div>
  <p>Lorem ipsum dolor sit amet, cctetr adipiscing elit, sed do eiusmod tepor incididunt ut labore et dolore magna aa. Quis ipsum suspendisse ultrces gravisus commodo viverra maecenas accumsan lacuvel facilisis. Lorem ipsum dolor sit amet, cctetr adipiscing</p>
  <div class="who">- Alex Moreno<span>Verified review</span></div><div class="badge"></div>
</div>
<div class="abs review" style="left:442px;top:3070px">
  <div class="quote">&ldquo;&ldquo;</div>
  <p>Lorem ipsum dolor sit amet, cctetr adipiscing elit, sed do eiusmod tepor incididunt ut labore et dolore magna aa. Quis ipsum suspendisse ultrces gravisus commodo viverra maecenas accumsan lacuvel facilisis. Lorem ipsum dolor sit amet, cctetr adipiscing</p>
  <div class="who">- Alex Moreno<span>Verified review</span></div><div class="badge"></div>
</div>
<div class="abs review" style="left:785px;top:3070px">
  <div class="quote">&ldquo;&ldquo;</div>
  <p>Lorem ipsum dolor sit amet, cctetr adipiscing elit, sed do eiusmod tepor incididunt ut labore et dolore magna aa. Quis ipsum suspendisse ultrces gravisus commodo viverra maecenas accumsan lacuvel facilisis. Lorem ipsum dolor sit amet, cctetr adipiscing</p>
  <div class="who">- Alex Moreno<span>Verified review</span></div><div class="badge"></div>
</div>
<div class="abs pager"><i></i><i class="on"></i><i></i><i></i></div>

<!-- HOW WE DO IT -->
<div class="abs" style="left:0;top:3514px;width:1200px">
  <h2 class="title"><b>HOW WE</b> DO IT</h2><div class="title-rule"></div>
</div>
<p class="abs intro" style="top:3596px">Lorem ipsum dolor sit amet, consectetur adipiscing elit, sed do eiusmod tempor incididunt ut labore et dolore magna aliqua. Quis ipsum suspendisse ultrices gravida. Risus commodo viverra maecenas</p>
<div class="abs how" style="left:100px;top:3699px">
  <div class="pic" role="img" aria-label="Photo of a business handshake at a desk" style="background:linear-gradient(135deg,#dfe3e6,#4a5a6a,#cfd6da)"></div>
  <div class="cap">Partnerships with farms in<br>COlombia, ecuador and costa rica</div>
</div>
<div class="abs how" style="left:440px;top:3699px">
  <div class="cap" style="font-size:15px">Farm fresh delivered directly from<br>cargo planes to state of the art<br>cooler facility at Delmont Airport</div>
  <div class="pic" role="img" aria-label="Photo of a cargo plane in a blue sky" style="background:linear-gradient(180deg,#6aa6d6,#cfe3f3)"></div>
</div>
<div class="abs how" style="left:781px;top:3699px">
  <div class="pic" role="img" aria-label="Photo of a green rainforest with mossy rocks" style="background:linear-gradient(135deg,#1f3a12,#6e9a2a,#2b4a1a)"></div>
  <div class="cap">Verity<br>Trust?</div>
</div>

<!-- CONTACT + FOOTER -->
<section class="abs night" role="img" aria-label="Dark photograph of flowers behind the contact area"></section>
<div class="abs" style="left:0;top:4224px;width:1200px">
  <h2 class="title" style="color:#fff"><b>GET</b> IN TOUCH</h2><div class="title-rule"></div>
</div>
<div class="abs field" style="left:284px;top:4302px;width:201px">Name</div>
<div class="abs field" style="left:499px;top:4302px;width:201px">Email</div>
<div class="abs field" style="left:713px;top:4302px;width:201px">Phone</div>
<div class="abs field" style="left:284px;top:4361px;width:630px;height:76px">Message</div>
<div class="abs btn" style="left:508px;top:4456px;width:184px;height:47px">SUBMIT</div>
<div class="abs" style="left:100px;top:4554px;width:1000px;height:1px;background:rgba(255,255,255,.15)"></div>

<div class="abs brand" style="left:99px;top:4620px;font-size:34px;line-height:36px;gap:16px">
  <span class="mark" style="width:96px;height:96px"></span>
  <span>MARLOWE<br>VANTAGE</span>
</div>
<div class="abs" style="left:145px;top:4746px;display:flex;gap:10px">
  <span class="social" aria-label="Social profile"></span><span class="social" aria-label="Social profile"></span><span class="social" aria-label="Social profile"></span><span class="social" aria-label="Social profile"></span>
</div>

<div class="abs footer-col" style="left:455px;top:4600px">
  <h4>QUICK LINKS</h4>
  <ul><li>Home</li><li>About Us</li><li>What We Do</li><li>How We Do It</li><li>Our Products</li><li>Contact Us</li></ul>
</div>
<div class="abs footer-col" style="left:643px;top:4600px">
  <h4>CUSTOMER SERVICES</h4>
  <ul><li>Privacy</li><li>Security</li><li>Terms of Service</li><li>Site Map</li><li>Careers</li></ul>
</div>
<div class="abs footer-col contact" style="left:880px;top:4600px">
  <h4>CONTACT INFO</h4>
  <ul>
    <li><svg width="10" height="13" viewBox="0 0 10 13"><path d="M5 0a5 5 0 0 1 5 5c0 3.5-5 8-5 8S0 8.5 0 5a5 5 0 0 1 5-5z" fill="#fff"/><circle cx="5" cy="5" r="2" fill="#24161b"/></svg><span>2180 Harbor Row Delmont,<br>MD 21044</span></li>
    <li class="name">GREGORY</li>
    <li><svg width="10" height="10" viewBox="0 0 24 24" fill="#fff"><path d="M6.6 10.8a15 15 0 0 0 6.6 6.6l2.2-2.2a1 1 0 0 1 1-.25 11 11 0 0 0 3.6.6 1 1 0 0 1 1 1V20a1 1 0 0 1-1 1A17 17 0 0 1 3 4a1 1 0 0 1 1-1h3.5a1 1 0 0 1 1 1 11 11 0 0 0 .6 3.6 1 1 0 0 1-.25 1z"/></svg><span>410-555-0147</span></li>
    <li><svg width="11" height="8" viewBox="0 0 14 10"><rect width="14" height="10" fill="#fff"/><path d="M0 0l7 6 7-6" stroke="#24161b" fill="none"/></svg><span>Gregory@marlowevantage.com</span></li>
    <li class="name">DANIELLE</li>
    <li><svg width="10" height="10" viewBox="0 0 24 24" fill="#fff"><path d="M6.6 10.8a15 15 0 0 0 6.6 6.6l2.2-2.2a1 1 0 0 1 1-.25 11 11 0 0 0 3.6.6 1 1 0 0 1 1 1V20a1 1 0 0 1-1 1A17 17 0 0 1 3 4a1 1 0 0 1 1-1h3.5a1 1 0 0 1 1 1 11 11 0 0 0 .6 3.6 1 1 0 0 1-.25 1z"/></svg><span>410-555-0182</span></li>
    <li><svg width="11" height="8" viewBox="0 0 14 10"><rect width="14" height="10" fill="#fff"/><path d="M0 0l7 6 7-6" stroke="#24161b" fill="none"/></svg><span>Danielle@marlowevantage.com</span></li>
  </ul>
</div>

<div class="abs" style="left:100px;top:4830px;width:1000px;height:1px;background:rgba(255,255,255,.15)"></div>
<p class="abs center" style="left:0;top:4846px;width:1200px;font-size:13px;color:#fff">Copyright © 2022 - Marlowe Vantage. All Right Reserved</p>
<div class="abs" style="left:1128px;top:4822px;width:42px;height:42px;border-radius:50%;background:#fff;display:flex;align-items:center;justify-content:center">
  <svg width="16" height="10" viewBox="0 0 16 10"><path d="M1 9l7-7 7 7" fill="none" stroke="#333" stroke-width="2"/></svg>
</div>

</body>
</html>
```